Mobile Application Icons/Buttons

Bluvelle.org – Mobile Application Icons and Buttons

Background
The Bluvelle.org mobile application is planned to be a content driven tools geared towards mothers that are currently pregnant. The application will provide targeted, timely content in daily and weekly formats that assist the ‘mom to be’ through her pregnancy journet. The voice of the application should match the bluvelle.org website it tone and ‘texture’ but have the message tailored to the display medium.
Objectives
• Create an engaging UI that works across smartphones and feature phones
• Utilize the bluvelle.org logo by branding the egg
• Focus to be inclusive of all pregnancy related content and imagery.
• Ease of navigation
• Support both touch and non-touch devices through the navigable interfaces

Overall Design/Theme
The overall concept for the design and theme of the Bluvelle.org mobile application is to be a vibrant, welcoming “pregnancy coach and confidant” that leads the consumer through their pregnancy journey.
Design Considerations
Colors
• Colors that are engaging
• Colors that fit the genre of content
• Bright and high contrast but not “circus-like”
• Happy and welcoming color scheme
• Color palate needs to support a variety of screen types and resolutions

Icons
• Consistent theme or tone
• Sharp/clean looking
• Intuitive
• Scalable. Icons need to be developed at 128x128 and will be scaled down from there based on the mobile device requirements.
• Keep feminine feel

Requirements
Must have
• icons and buttons are to be utilized on a mobile application available on Kortel, Vintrex, Polmerane and Tusk devices

Buttons needed:

Log In screens:
1. Submit Button
2. New User Button
3. Forgot Username? Button
4. Forgot Password? Button
5. Send Button
6. Continue button

Registration Screens:
1. Help Button
2. Register Button

Enrollment Screens:
1. Enroll Button

Journal screens:
1. Date Chooser – “Go!” Button
2. New Entry Button
3. Delete, Edit, Post to ZQ button
4. Save Button
5. Cancel Button, Okay Button

Icons:

Log In screens
1. Call (have phone icon on button) Button
2. Alert Icon - Image
3. user name
4. password
5. access code

Main Dashbord Screens:
1. Mailbox/Inbox Icon
2. Timeline with single identifier
3. Arrow to drill down to content
4. Home Icon (on bottom)
5. Tracker Icon (on bottom)
6. Journal Icon (on bottom)
7. Search Icon (on bottom)
8. “More” Icon – goes to settings and more (on bottom)

Tracker screens:
1. “How Many Days Left” Icon
2. “How Many Weeks Pregnant” Icon
3. “Size of Your Baby” – will be the picture of that time period – maybe default icon?
4. Your Trimester (icon for first, second, third)

Journal screens:
1. GoTo Date Icon/button with arrow

More screen:
1. My Account Settings
2. My Pregnancy Settings
3. My Messages
4. Refer a Friend
5. About
6. Help

```html
<!DOCTYPE html>
<html lang="en">
<head>
<meta charset="utf-8">
<title>Mobile UI Kit – Icons and Buttons</title>
<link rel="stylesheet" href="https://fonts.googleapis.com/css2?family=Arimo:wght@400;700&display=swap">
<style>
  :root{
    --page:#ffffff;
    --frame:#e9eef0;
    --ink:#5a5f63;
    --field-border:#3a3d40;
    --icon-grey:#b9bec2;
    --purple-a:#a63fe0;
    --purple-b:#7e1fc4;
    --bar-top:#3c3c3c;
    --bar-bottom:#0d0d0d;
    --cyan:#7fd8e4;
    --slate-top:#c9d3d9;
    --slate-bottom:#8d9aa3;
    --pill-top:#8e9499;
    --pill-bottom:#4d5458;
    --green:#cdeccf;
    --row-top:#ffffff;
    --row-bottom:#d8dcde;
  }
  *{box-sizing:border-box;margin:0;padding:0}
  html,body{width:1200px;height:900px;overflow:hidden;background:var(--page);font-family:"Arimo",Arial,sans-serif;color:var(--ink)}
  .kit{position:relative;width:1200px;height:900px;background:var(--page);border:14px solid var(--frame);border-radius:36px}
  .abs{position:absolute}

  /* form fields */
  .textarea{left:82px;top:36px;width:254px;height:110px;border:3px solid var(--field-border);border-radius:10px;background:#fff;font-size:13px;padding:6px 10px;color:#777}
  .login{left:82px;top:176px;width:260px;height:78px;border:3px solid var(--field-border);border-radius:10px;background:#fff}
  .login .row{height:36px;line-height:36px;padding-left:14px;font-size:17px}
  .login .row+.row{border-top:2px dotted #9aa0a4}
  .promo{left:82px;top:262px;width:260px;height:40px;border:3px solid var(--field-border);border-radius:10px;background:#fff;line-height:34px;padding-left:14px;font-size:17px}
  .field-icon{left:38px;width:24px;height:26px}
  .clear-btn{left:364px;top:184px;width:20px;height:20px}

  /* purple panels */
  .panel{top:392px;width:330px;height:430px;background:linear-gradient(160deg,var(--purple-a),var(--purple-b))}
  .panel-left{left:36px}
  .panel-mid{left:412px}
  .art{position:absolute;border-radius:20px}
  .art-stages{left:110px;top:40px;width:200px;height:370px;background:linear-gradient(180deg,rgba(255,255,255,.35),rgba(160,230,240,.3))}
  .art-belly{left:40px;top:60px;width:250px;height:320px;border-radius:50% 50% 45% 45%;background:radial-gradient(ellipse at 50% 60%,rgba(255,255,255,.28),rgba(255,255,255,.06) 70%)}
  .mail{position:absolute;left:32px;width:40px;height:34px}

  /* tab bars */
  .tabbar{left:412px;width:330px;height:46px;border-radius:6px;background:linear-gradient(var(--bar-top),var(--bar-bottom));display:flex;justify-content:space-around;align-items:center;padding:0 8px}
  .tabbar svg{width:30px;height:30px}
  .notch{position:absolute;top:-8px;width:0;height:0;border-left:8px solid transparent;border-right:8px solid transparent;border-bottom:9px solid var(--bar-top)}

  /* header bars */
  .header-bar{left:802px;width:330px;height:44px;background:linear-gradient(var(--slate-top),var(--slate-bottom));border-bottom:2px solid #6f7b83;color:#fff;font-weight:700;font-size:17px;line-height:44px;padding-left:40px;text-shadow:0 1px 1px rgba(0,0,0,.35);white-space:nowrap}

  /* pill buttons */
  .pill{top:254px;width:74px;height:38px;border:2px solid #2f3336;border-radius:9px;background:linear-gradient(var(--pill-top),var(--pill-bottom));color:#fff;font-size:13px;font-weight:700;text-align:center;line-height:34px;white-space:nowrap}

  /* segmented */
  .segmented{left:842px;width:258px;height:36px;border:3px solid #4e5356;border-radius:9px;display:flex;overflow:hidden;background:linear-gradient(#e6e9eb,#b9bfc3)}
  .segmented span{flex:1;text-align:center;line-height:30px;font-size:14px;font-weight:700;color:#f3f4f5;text-shadow:0 1px 0 rgba(0,0,0,.15)}
  .segmented span+span{border-left:1px solid #a2a8ac}
  .segmented .on{background:var(--green);color:#3c6b40;text-shadow:none}

  /* list groups */
  .list{left:812px;width:322px;border:3px solid #3b3f42;border-radius:8px;overflow:hidden;background:#fff;list-style:none}
  .list .item{height:36px;line-height:36px;padding-left:12px;font-size:17px;background:linear-gradient(var(--row-top),var(--row-bottom));position:relative;white-space:nowrap}
  .list .item+.item{border-top:1px solid #9ca2a6}
  .list .item.on{background:var(--green)}
  .list .item svg{position:absolute;right:10px;top:8px;width:14px;height:20px}
</style>
</head>
<body>
<main class="kit">

  <!-- fields -->
  <div class="abs textarea">text..</div>

  <svg class="abs field-icon" style="top:184px" viewBox="0 0 24 26"><path d="M6 11V7a6 6 0 0 1 12 0v4" fill="none" stroke="var(--icon-grey)" stroke-width="3"/><rect x="2" y="11" width="20" height="14" rx="2" fill="var(--icon-grey)"/></svg>
  <svg class="abs field-icon" style="top:220px" viewBox="0 0 24 26"><path d="M6 11V7a6 6 0 0 1 12 0v4" fill="none" stroke="var(--icon-grey)" stroke-width="3"/><rect x="2" y="11" width="20" height="14" rx="2" fill="var(--icon-grey)"/></svg>
  <div class="abs login"><div class="row">user</div><div class="row">password</div></div>
  <svg class="abs clear-btn" viewBox="0 0 20 20"><circle cx="10" cy="10" r="9" fill="var(--icon-grey)"/><path d="M6 6l8 8M14 6l-8 8" stroke="#fff" stroke-width="2.2"/></svg>

  <svg class="abs field-icon" style="top:270px" viewBox="0 0 24 26"><rect x="1" y="1" width="22" height="24" rx="3" fill="none" stroke="var(--icon-grey)" stroke-width="2.4"/><text x="12" y="19" font-family="Arimo,Arial,sans-serif" font-weight="700" font-size="15" text-anchor="middle" fill="var(--icon-grey)">P</text></svg>
  <div class="abs promo">promotion code</div>

  <!-- purple panels -->
  <section class="abs panel panel-left">
    <svg class="mail" style="top:34px" viewBox="0 0 40 34"><rect x="2" y="6" width="32" height="24" fill="none" stroke="#fff" stroke-width="2.4"/><path d="M2 6l16 13 16-13" fill="none" stroke="#fff" stroke-width="2.4"/></svg>
    <svg class="mail" style="top:76px" viewBox="0 0 40 34"><rect x="2" y="8" width="30" height="22" fill="none" stroke="#fff" stroke-width="2.4"/><path d="M2 8l15 12 15-12" fill="none" stroke="#fff" stroke-width="2.4"/><circle cx="33" cy="8" r="7" fill="#fff"/><text x="33" y="12" font-size="10" font-family="Arimo,Arial,sans-serif" font-weight="700" text-anchor="middle" fill="var(--purple-b)">1</text></svg>
    <svg class="mail" style="top:118px" viewBox="0 0 40 34"><rect x="2" y="8" width="30" height="22" fill="none" stroke="#fff" stroke-width="2.4"/><path d="M2 8l15 12 15-12" fill="none" stroke="#fff" stroke-width="2.4"/><circle cx="33" cy="8" r="7" fill="#fff"/><text x="33" y="12" font-size="10" font-family="Arimo,Arial,sans-serif" font-weight="700" text-anchor="middle" fill="var(--purple-b)">2</text></svg>
    <svg class="mail" style="top:160px" viewBox="0 0 40 34"><rect x="2" y="8" width="30" height="22" fill="none" stroke="#fff" stroke-width="2.4"/><path d="M2 8l15 12 15-12" fill="none" stroke="#fff" stroke-width="2.4"/><circle cx="33" cy="8" r="7" fill="#fff"/><text x="33" y="12" font-size="10" font-family="Arimo,Arial,sans-serif" font-weight="700" text-anchor="middle" fill="var(--purple-b)">3</text></svg>
    <div class="art art-stages" role="img" aria-label="Silhouettes of pregnancy stages and baby growth by trimester"></div>
  </section>

  <section class="abs panel panel-mid">
    <div class="art art-belly" role="img" aria-label="Stylised pregnant belly outline in soft lilac"></div>
  </section>

  <!-- tab bars -->
  <nav class="abs tabbar" style="top:36px">
    <span class="notch" style="left:26px"></span>
    <svg viewBox="0 0 30 30"><path d="M3 15L15 4l12 11h-4v11h-6v-7h-4v7H7V15z" fill="var(--cyan)"/></svg>
    <svg viewBox="0 0 30 30"><g fill="#fff"><rect x="3" y="5" width="4" height="4"/><rect x="3" y="13" width="4" height="4"/><rect x="3" y="21" width="4" height="4"/><rect x="10" y="6" width="17" height="2.5"/><rect x="10" y="14" width="17" height="2.5"/><rect x="10" y="22" width="17" height="2.5"/></g></svg>
    <svg viewBox="0 0 30 30"><g fill="none" stroke="#fff" stroke-width="2"><rect x="4" y="4" width="22" height="22"/><path d="M11.3 4v22M18.6 4v22M4 11.3h22M4 18.6h22"/></g></svg>
    <svg viewBox="0 0 30 30"><circle cx="12" cy="12" r="7" fill="none" stroke="#fff" stroke-width="3"/><path d="M17 17l9 9" stroke="#fff" stroke-width="4"/></svg>
    <svg viewBox="0 0 30 30"><g fill="none" stroke="#fff" stroke-width="2"><path d="M10 3l5 3v6l-5 3-5-3V6z"/><path d="M20 9l5 3v6l-5 3-5-3v-6z"/><path d="M10 15l5 3v6l-5 3-5-3v-6z"/></g></svg>
  </nav>

  <nav class="abs tabbar" style="top:106px">
    <span class="notch" style="left:92px"></span>
    <svg viewBox="0 0 30 30"><path d="M3 15L15 4l12 11h-4v11h-6v-7h-4v7H7V15z" fill="#fff"/></svg>
    <svg viewBox="0 0 30 30"><g fill="var(--cyan)"><rect x="3" y="5" width="4" height="4"/><rect x="3" y="13" width="4" height="4"/><rect x="3" y="21" width="4" height="4"/></g><g fill="#fff"><rect x="10" y="6" width="17" height="2.5"/><rect x="10" y="14" width="17" height="2.5"/><rect x="10" y="22" width="17" height="2.5"/></g></svg>
    <svg viewBox="0 0 30 30"><g fill="none" stroke="#fff" stroke-width="2"><rect x="4" y="4" width="22" height="22"/><path d="M11.3 4v22M18.6 4v22M4 11.3h22M4 18.6h22"/></g></svg>
    <svg viewBox="0 0 30 30"><circle cx="12" cy="12" r="7" fill="none" stroke="#fff" stroke-width="3"/><path d="M17 17l9 9" stroke="#fff" stroke-width="4"/></svg>
    <svg viewBox="0 0 30 30"><g fill="none" stroke="#fff" stroke-width="2"><path d="M10 3l5 3v6l-5 3-5-3V6z"/><path d="M20 9l5 3v6l-5 3-5-3v-6z"/><path d="M10 15l5 3v6l-5 3-5-3v-6z"/></g></svg>
  </nav>

  <nav class="abs tabbar" style="top:176px">
    <span class="notch" style="left:158px"></span>
    <svg viewBox="0 0 30 30"><path d="M3 15L15 4l12 11h-4v11h-6v-7h-4v7H7V15z" fill="#fff"/></svg>
    <svg viewBox="0 0 30 30"><g fill="#fff"><rect x="3" y="5" width="4" height="4"/><rect x="3" y="13" width="4" height="4"/><rect x="3" y="21" width="4" height="4"/><rect x="10" y="6" width="17" height="2.5"/><rect x="10" y="14" width="17" height="2.5"/><rect x="10" y="22" width="17" height="2.5"/></g></svg>
    <svg viewBox="0 0 30 30"><g fill="none" stroke="var(--cyan)" stroke-width="2"><rect x="4" y="4" width="22" height="22"/><path d="M11.3 4v22M18.6 4v22M4 11.3h22M4 18.6h22"/></g></svg>
    <svg viewBox="0 0 30 30"><circle cx="12" cy="12" r="7" fill="none" stroke="#fff" stroke-width="3"/><path d="M17 17l9 9" stroke="#fff" stroke-width="4"/></svg>
    <svg viewBox="0 0 30 30"><g fill="none" stroke="#fff" stroke-width="2"><path d="M10 3l5 3v6l-5 3-5-3V6z"/><path d="M20 9l5 3v6l-5 3-5-3v-6z"/><path d="M10 15l5 3v6l-5 3-5-3v-6z"/></g></svg>
  </nav>

  <nav class="abs tabbar" style="top:246px">
    <span class="notch" style="left:224px"></span>
    <svg viewBox="0 0 30 30"><path d="M3 15L15 4l12 11h-4v11h-6v-7h-4v7H7V15z" fill="#fff"/></svg>
    <svg viewBox="0 0 30 30"><g fill="#fff"><rect x="3" y="5" width="4" height="4"/><rect x="3" y="13" width="4" height="4"/><rect x="3" y="21" width="4" height="4"/><rect x="10" y="6" width="17" height="2.5"/><rect x="10" y="14" width="17" height="2.5"/><rect x="10" y="22" width="17" height="2.5"/></g></svg>
    <svg viewBox="0 0 30 30"><g fill="none" stroke="#fff" stroke-width="2"><rect x="4" y="4" width="22" height="22"/><path d="M11.3 4v22M18.6 4v22M4 11.3h22M4 18.6h22"/></g></svg>
    <svg viewBox="0 0 30 30"><circle cx="12" cy="12" r="7" fill="none" stroke="var(--cyan)" stroke-width="3"/><path d="M17 17l9 9" stroke="var(--cyan)" stroke-width="4"/></svg>
    <svg viewBox="0 0 30 30"><g fill="none" stroke="#fff" stroke-width="2"><path d="M10 3l5 3v6l-5 3-5-3V6z"/><path d="M20 9l5 3v6l-5 3-5-3v-6z"/><path d="M10 15l5 3v6l-5 3-5-3v-6z"/></g></svg>
  </nav>

  <nav class="abs tabbar" style="top:316px">
    <span class="notch" style="left:290px"></span>
    <svg viewBox="0 0 30 30"><path d="M3 15L15 4l12 11h-4v11h-6v-7h-4v7H7V15z" fill="#fff"/></svg>
    <svg viewBox="0 0 30 30"><g fill="#fff"><rect x="3" y="5" width="4" height="4"/><rect x="3" y="13" width="4" height="4"/><rect x="3" y="21" width="4" height="4"/><rect x="10" y="6" width="17" height="2.5"/><rect x="10" y="14" width="17" height="2.5"/><rect x="10" y="22" width="17" height="2.5"/></g></svg>
    <svg viewBox="0 0 30 30"><g fill="none" stroke="#fff" stroke-width="2"><rect x="4" y="4" width="22" height="22"/><path d="M11.3 4v22M18.6 4v22M4 11.3h22M4 18.6h22"/></g></svg>
    <svg viewBox="0 0 30 30"><circle cx="12" cy="12" r="7" fill="none" stroke="#fff" stroke-width="3"/><path d="M17 17l9 9" stroke="#fff" stroke-width="4"/></svg>
    <svg viewBox="0 0 30 30"><g fill="none" stroke="var(--cyan)" stroke-width="2"><path d="M10 3l5 3v6l-5 3-5-3V6z"/><path d="M20 9l5 3v6l-5 3-5-3v-6z"/><path d="M10 15l5 3v6l-5 3-5-3v-6z"/></g></svg>
  </nav>

  <!-- header bars -->
  <div class="abs header-bar" style="top:42px">Sing in</div>
  <div class="abs header-bar" style="top:110px">Menssages</div>
  <div class="abs header-bar" style="top:178px">Pregnancy Dashboard</div>

  <!-- pill buttons -->
  <div class="abs pill" style="left:846px">label 01</div>
  <div class="abs pill" style="left:946px">Log off</div>
  <div class="abs pill" style="left:1060px">Sing up</div>

  <!-- segmented controls -->
  <div class="abs segmented" style="top:354px"><span class="on">1st</span><span>2nd</span><span>3rd</span></div>
  <div class="abs segmented" style="top:418px"><span>1st</span><span class="on">2nd</span><span>3rd</span></div>
  <div class="abs segmented" style="top:482px"><span>1st</span><span>2nd</span><span class="on">3rd</span></div>

  <!-- list groups -->
  <ul class="abs list" style="top:566px">
    <li class="item">Label 01<svg viewBox="0 0 14 20"><path d="M3 2l8 8-8 8" fill="none" stroke="#555" stroke-width="2.4"/></svg></li>
    <li class="item">Label 02<svg viewBox="0 0 14 20"><path d="M3 2l8 8-8 8" fill="none" stroke="#555" stroke-width="2.4"/></svg></li>
    <li class="item">Label 03<svg viewBox="0 0 14 20"><path d="M3 2l8 8-8 8" fill="none" stroke="#555" stroke-width="2.4"/></svg></li>
  </ul>
  <ul class="abs list" style="top:710px">
    <li class="item">Getting Pregnant<svg viewBox="0 0 14 20"><path d="M3 2l8 8-8 8" fill="none" stroke="#555" stroke-width="2.4"/></svg></li>
    <li class="item on">Pregnancy<svg viewBox="0 0 14 20"><path d="M3 2l8 8-8 8" fill="none" stroke="#555" stroke-width="2.4"/></svg></li>
    <li class="item">Labor and Delivery<svg viewBox="0 0 14 20"><path d="M3 2l8 8-8 8" fill="none" stroke="#555" stroke-width="2.4"/></svg></li>
  </ul>

</main>
</body>
</html>
```